Dental Business Card

I need Dental oriented business cards.
On the front side -
- on the first line, my name:
Dr Marlo Vintner
- on the second line (just underneath):
Doctor of Dental Medicine
- on the third line, or underneath that or in a corner, I would like the address and phone number:
5182 Ch. Birchfield
Montreal QC H2T 4B9
514-629-5074
- other than that i would maybe like a logo of a tooth, but i want it to be subtle and very basic!
- I would like the card to be preferably black or dark grey-ish with the writing in white
On the other side -
- 2-3 lines with the possibility to write the next appointment the box with the lines should be white, with the rest of the card being black

```html
<!DOCTYPE html>
<html lang="en">
<head>
<meta charset="utf-8">
<title>Dental Business Card – Dr Marlo Vintner</title>
<link rel="stylesheet" href="https://fonts.googleapis.com/css2?family=Electrolize&display=swap">
<style>
  :root {
    --page: #ffffff;
    --card: #0e0e0e;
    --ink: #ffffff;
    --gold: #e8c98f;
    --tooth-light: #eef0f2;
    --tooth-cream: #f6d7a7;
    --write-box: #ffffff;
    --write-line: #b9b9b9;
  }
  * { margin: 0; padding: 0; box-sizing: border-box; }
  html, body {
    width: 1200px; height: 1200px; overflow: hidden;
    background: var(--page);
    font-family: "Electrolize", sans-serif;
    color: var(--ink);
  }
  .card {
    position: absolute; left: 208px; width: 834px; height: 539px;
    background: var(--card);
  }
  .card--front { top: 83px; }
  .card--back { top: 642px; }
  .card__frame { position: absolute; inset: 0; }
  .front__name {
    position: absolute; right: 282px; top: 128px;
    font-size: 38px; letter-spacing: 0.6px; white-space: nowrap;
  }
  .front__title, .back__title {
    position: absolute; font-size: 23px; letter-spacing: 1.2px; white-space: nowrap;
  }
  .front__title { right: 281px; top: 183px; }
  .front__rule {
    position: absolute; left: 239px; top: 220px; width: 318px; height: 2px;
    background: var(--gold);
  }
  .front__address {
    position: absolute; right: 271px; top: 294px; text-align: right;
    font-size: 22px; line-height: 29px; letter-spacing: 2.6px; white-space: nowrap;
  }
  .front__phone {
    position: absolute; right: 278px; top: 367px;
    font-size: 22px; letter-spacing: 0.4px;
  }
  .logo-area {
    position: absolute; border-radius: 40% 40% 30% 30%;
    background: linear-gradient(100deg, var(--tooth-light) 0 58%, var(--tooth-cream) 58% 100%);
  }
  .front__logo { left: 627px; top: 112px; width: 110px; height: 115px; }
  .back__logo { left: 322px; top: 176px; width: 188px; height: 185px; }
  .back__title { left: 0; right: 0; top: 369px; text-align: center; padding-right: 32px; }
  .appointment-box {
    position: absolute; left: 217px; top: 408px; width: 368px; height: 62px;
    background: var(--write-box); border-radius: 3px;
    padding: 0 18px;
  }
  .appointment-box__line {
    position: absolute; left: 18px; right: 18px; height: 1px;
    background: var(--write-line);
  }
  .appointment-box__line:nth-child(1) { top: 24px; }
  .appointment-box__line:nth-child(2) { top: 46px; }
</style>
</head>
<body>
  <section class="card card--front">
    <svg class="card__frame" width="834" height="539" viewBox="0 0 834 539" fill="none" stroke="var(--gold)" stroke-width="2">
      <path d="M60 30 H772 V42 H802 V479 H772 V509 H60 V479 H30 V42 H60 Z"/>
      <rect x="40" y="39" width="9" height="9"/><rect x="48" y="46" width="9" height="9"/>
      <rect x="785" y="39" width="9" height="9"/><rect x="777" y="46" width="9" height="9"/>
      <rect x="40" y="490" width="9" height="9"/><rect x="48" y="483" width="9" height="9"/>
      <rect x="785" y="490" width="9" height="9"/><rect x="777" y="483" width="9" height="9"/>
    </svg>
    <div class="front__name">Dr Marlo Vintner</div>
    <div class="front__title">Doctor of Dental Medicine</div>
    <div class="front__rule"></div>
    <div class="front__address">5182 Ch. Birchfield Montreal<br>QC H2T 4B9</div>
    <div class="front__phone">514-629-5074</div>
    <div class="logo-area front__logo" role="img" aria-label="Tooth logo: a large white tooth with a small cream tooth"></div>
  </section>

  <section class="card card--back">
    <svg class="card__frame" width="834" height="539" viewBox="0 0 834 539" fill="none" stroke="var(--gold)" stroke-width="2">
      <path d="M60 30 H772 V42 H802 V479 H772 V509 H60 V479 H30 V42 H60 Z"/>
      <rect x="40" y="39" width="9" height="9"/><rect x="48" y="46" width="9" height="9"/>
      <rect x="785" y="39" width="9" height="9"/><rect x="777" y="46" width="9" height="9"/>
      <rect x="40" y="490" width="9" height="9"/><rect x="48" y="483" width="9" height="9"/>
      <rect x="785" y="490" width="9" height="9"/><rect x="777" y="483" width="9" height="9"/>
    </svg>
    <div class="logo-area back__logo" role="img" aria-label="Tooth logo: a large white tooth with a small cream tooth"></div>
    <div class="back__title">Doctor of Dental Medicine</div>
    <div class="appointment-box" aria-label="Space to write the next appointment">
      <div class="appointment-box__line"></div>
      <div class="appointment-box__line"></div>
    </div>
  </section>
</body>
</html>
```